Website for Private Psychologist

DO NOT CONTACT ME PRIVATELY

I am a Psychologist offering psychotherapy for individuals and couples, and clinical consultation and training and education for mental and medical health professionals and agencies.

I need a redesign of my website

5 Pages (content is attached for each page)
Home
Jungian Psychotherapy
Clinical Consultation & Professional Development
Curriculum Vitae & Publications
Practice Policies and Forms

Designs can be based on these style websites
https://velmorcare.info; https://brantomind.org/; https://dorelhaskettpsychotherapy.com/

Minimalist Layout: Clean and uncluttered layout with generous white space, allowing the content and visuals to stand out'

Keep a linear, uncluttered, professional design.

Please use only royalty free images and google fonts. Please provide links to any stock images used to verify license.

private individual or couples seeking psychotherapy

Psychotherapy

5+ page

• No search feature

```html
<!DOCTYPE html>
<html lang="en">
<head>
<meta charset="utf-8">
<title>Dorian Vellacourt, Psy.D. – Psychologist</title>
<link href="https://fonts.googleapis.com/css2?family=Playfair+Display:wght@400;500;600;700&family=Poppins:wght@400;500;600&family=Inter:wght@400;500;600&display=swap" rel="stylesheet">
<style>
:root{
  --purple:#633a98;
  --green:#087a4a;
  --ink:#1e1e1e;
  --body:#4a4a4a;
  --mint:#d2ebee;
  --footer:#1b1b1b;
  --white:#ffffff;
}
*{box-sizing:border-box;margin:0;padding:0}
html,body{width:1200px;height:2832px;overflow:hidden}
body{position:relative;font-family:"Inter",sans-serif;color:var(--ink);background:var(--white)}
.abs{position:absolute}
.serif{font-family:"Playfair Display",serif}

/* header */
.logo{font-family:"Playfair Display",serif;font-weight:700;color:var(--purple);text-decoration:underline;text-underline-offset:4px;text-decoration-thickness:2px;white-space:nowrap}
.header-logo{left:101px;top:6px;font-size:34px}
.btn-outline{border:1px solid var(--green);border-radius:3px;color:var(--green);font-family:"Poppins",sans-serif;font-size:13px;font-weight:500;display:flex;align-items:center;justify-content:center;gap:6px;background:var(--white);white-space:nowrap}
.btn-phone{left:821px;top:12px;width:144px;height:35px}
.btn-contact{left:974px;top:12px;width:125px;height:35px}
.nav{left:0;top:60px;width:1200px;height:37px;background:var(--purple);display:flex;align-items:center;padding:0 101px;justify-content:space-between;font-family:"Poppins",sans-serif;font-size:14px;font-weight:600;color:var(--white);white-space:nowrap}

/* hero */
.hero{left:0;top:97px;width:1200px;height:625px;background:radial-gradient(circle at 765px 260px,#c6e4c3 0,#8fcab7 120px,#3b6a6a 230px,#25302f 380px,#1d2121 100%)}
.hero-title{left:99px;top:296px;font-size:60px;font-weight:700;color:var(--white)}
.hero-text{left:99px;top:378px;width:360px;font-family:"Poppins",sans-serif;font-size:15.5px;line-height:28px;color:var(--white)}
.btn-solid{background:var(--green);color:var(--white);font-family:"Inter",sans-serif;font-weight:600;font-size:14px;display:flex;align-items:center;justify-content:center;border-radius:2px;letter-spacing:.2px;white-space:nowrap}
.hero-btn{left:99px;top:455px;width:200px;height:40px}
.dots{left:558px;top:680px;display:flex;gap:11px}
.dots span{width:13px;height:13px;border:1.5px solid var(--white);border-radius:50%}
.dots span.on{background:var(--white)}

/* about */
.photo-back{left:155px;top:806px;width:428px;height:448px;background:var(--purple);border-radius:22px}
.photo{left:137px;top:793px;width:428px;height:444px;border-radius:22px;background:linear-gradient(160deg,#6f6a62,#3a352f 55%,#242220)}
.caption{left:200px;top:1211px;width:288px;height:51px;background:var(--white);box-shadow:0 4px 10px rgba(0,0,0,.15);font-size:21px;display:flex;align-items:center;justify-content:center;white-space:nowrap}
.h2{font-family:"Playfair Display",serif;font-weight:500;font-size:38px;line-height:43px;color:var(--ink)}
.about-title{left:639px;top:868px;width:460px}
.para{font-size:12.5px;line-height:29px;color:var(--body);text-align:justify}
.about-text{left:639px;top:970px;width:425px}
.about-btn{left:639px;top:1133px;width:150px;height:40px}

/* specializations */
.spec{left:0;top:1336px;width:1200px;height:594px;background:var(--mint)}
.spec-title{left:0;top:1396px;width:1200px;text-align:center}
.arch{top:1467px;width:312px;height:293px;border-radius:156px 156px 0 0}
.card{top:1736px;width:293px;height:121px;background:var(--white);padding:12px 12px;box-shadow:0 2px 8px rgba(0,0,0,.06)}
.card h3{font-size:16px;font-weight:600;color:var(--purple);margin-bottom:5px;white-space:nowrap}
.card p{font-size:12.5px;line-height:23px;color:var(--body)}

/* booking */
.book-title{left:99px;top:2030px;width:560px;font-size:37px;white-space:nowrap}
.book-text{left:99px;top:2133px;width:478px}
.choose{left:100px;top:2264px;font-size:15px}
.plan{top:2302px;width:187px;height:55px;background:var(--purple);border-radius:3px;color:var(--white);font-size:14.5px;font-weight:500;padding:8px 0 0 19px;line-height:20px;white-space:nowrap}
.form{left:662px;top:1995px;width:437px;height:407px;background:var(--purple);border-radius:10px}
.form-title{left:662px;top:2012px;width:437px;text-align:center;font-family:"Playfair Display",serif;font-size:34px;font-weight:500;color:var(--white);white-space:nowrap}
.field{left:683px;width:395px;height:38px;background:var(--white);font-size:13px;color:#666;padding:11px 13px}
.submit{left:806px;top:2336px;width:150px;height:39px}

/* footer */
.footer{left:0;top:2468px;width:1200px;height:364px;background:var(--footer)}
.footer-logo{left:99px;top:2545px;font-size:27px;color:var(--white)}
.social{top:2588px;width:40px;height:40px;border:1.5px solid var(--white);border-radius:50%}
.col-h{top:2536px;font-size:16px;font-weight:600;color:var(--white);border-bottom:2px solid var(--white);padding-bottom:3px;white-space:nowrap}
.col{font-size:14.5px;line-height:26px;color:var(--white);white-space:nowrap}
.links{font-family:"Poppins",sans-serif;font-weight:600;font-size:14px;line-height:29px}
.contact-row{display:flex;gap:8px;align-items:flex-start}
.rule{left:97px;top:2773px;width:1006px;height:1px;background:#555}
.copy{left:0;top:2786px;width:1200px;text-align:center;font-size:14.5px;color:var(--white)}
</style>
</head>
<body>

<a class="abs logo header-logo">Dorian Vellacourt, Psy.D.</a>
<div class="abs btn-outline btn-phone">
  <svg width="14" height="14" viewBox="0 0 24 24" fill="none" stroke="#087a4a" stroke-width="2"><path d="M5 3h4l2 5-2.5 1.5a11 11 0 0 0 6 6L16 13l5 2v4a2 2 0 0 1-2 2A16 16 0 0 1 3 5a2 2 0 0 1 2-2z"/></svg>
  (415) 555-0187
</div>
<div class="abs btn-outline btn-contact">CONTACT US</div>
<nav class="abs nav">
  <span>Jungian Psychotherapy</span>
  <span>Clinical Consultation &amp; Professional Development</span>
  <span>Curriculum Vitae &amp; Publications</span>
  <span>Practice Policies</span>
</nav>

<section class="abs hero" role="img" aria-label="Painting of a cave opening shaped like a human head in profile, with a branching tree and misty green hills beyond"></section>
<h1 class="abs serif hero-title">Psychologist</h1>
<p class="abs hero-text">Lorem ipsum dolor sit amet, conur adipiscing elit, sed do eiusmod tempor</p>
<div class="abs btn-solid hero-btn">BOOK A CONSULTATION</div>
<div class="abs dots"><span></span><span></span><span class="on"></span><span></span></div>

<div class="abs photo-back"></div>
<div class="abs photo" role="img" aria-label="Portrait photograph of the psychologist wearing glasses and a dark sweater"></div>
<div class="abs caption">Dorian Vellacourt, Psy.D.</div>
<h2 class="abs h2 about-title">Jungian Psychotherapy &amp;<br>Consultation</h2>
<p class="abs para about-text">I am a California Licensed Psychologist with an office in the San Francisco Financial District offering psychotherapy for individuals and couples, and clinical consultation and training and education for mental and medical health professionals and agencies. All appointments are currently available via telehealth.</p>
<div class="abs btn-solid about-btn">LEARN MORE</div>

<section class="abs spec"></section>
<h2 class="abs h2 spec-title">Specializations</h2>

<div class="abs arch" style="left:100px;background:linear-gradient(180deg,#8a5d50,#5a3a35 60%,#3d2a28)" role="img" aria-label="Hands holding up a green smiling face and a red frowning face"></div>
<div class="abs card" style="left:109px"><h3>Disorder Assessment &amp; Treatment</h3><p>Sed ut perspiciatis unde ois ir sit voluptatem accutium doloremque laudium, totam rem aperiam, eaque ipsa quae ab</p></div>

<div class="abs arch" style="left:444px;background:linear-gradient(180deg,#9a7a55,#4a3322 55%,#2a1d16)" role="img" aria-label="Speaker with a microphone facing a seated audience"></div>
<div class="abs card" style="left:453px"><h3>Motivational Interviewing</h3><p>Sed ut perspiciatis unde ois ir sit voluptatem accutium doloremque laudium, totam rem aperiam, eaque ipsa quae ab</p></div>

<div class="abs arch" style="left:788px;background:linear-gradient(180deg,#e4e4e2,#b8c4c8 55%,#7b8fa0)" role="img" aria-label="Two women sitting together in a counseling session"></div>
<div class="abs card" style="left:797px"><h3>Treatment Issues Specific To LGBT</h3><p>Sed ut perspiciatis unde ois ir sit voluptatem accutium doloremque laudium, totam rem aperiam, eaque ipsa quae ab</p></div>

<h2 class="abs h2 book-title">Ready to discuss your problem<br>with the right Counselor?</h2>
<p class="abs para book-text">Sed ut perspiciatis unde omnis iste natus error sit voluptatem accusantium doloremque laudantium, totam rem aperiam, eaque ipsa quae ab illo inventore veritatis et quasi architecto beatae vitae dicta sunt explicabo. Nemo enim ipsam voluptatem quia voluptas sit aspernatur aut odit aut fugit</p>
<p class="abs choose">Choose the type of counseling</p>
<div class="abs plan" style="left:100px">Individual Counseling<br>$15/session</div>
<div class="abs plan" style="left:299px">Couples Counseling<br>$25/session</div>

<div class="abs form"></div>
<div class="abs form-title">Session Scheduling Form</div>
<div class="abs field" style="top:2074px">Your name here</div>
<div class="abs field" style="top:2124px">Your email here</div>
<div class="abs field" style="top:2174px">Phone number</div>
<div class="abs field" style="top:2224px;height:93px">Message</div>
<div class="abs btn-solid submit">SUBMIT</div>

<footer class="abs footer"></footer>
<div class="abs logo footer-logo">Dorian Vellacourt, Psy.D.</div>
<div class="abs social" style="left:153px"></div>
<div class="abs social" style="left:200px"></div>
<div class="abs social" style="left:246px"></div>
<div class="abs social" style="left:293px"></div>

<div class="abs col-h" style="left:454px">QUICK LINKS</div>
<div class="abs col links" style="left:454px;top:2573px">
  Jungian Psychotherapy<br>&nbsp;Clinical Consultation &amp;<br>Professional Development<br>Curriculum Vitae &amp; Publications<br>Practice Policies
</div>

<div class="abs col-h" style="left:725px">RESOURCES</div>
<div class="abs col" style="left:725px;top:2575px">Carrers<br>Awards<br>FAQ<br>Media &amp; Press<br>Video Libeary</div>

<div class="abs col-h" style="left:887px">CONTACT US</div>
<div class="abs col" style="left:887px;top:2576px;width:220px;line-height:22px">
  <div class="contact-row"><svg width="17" height="20" viewBox="0 0 24 24" fill="none" stroke="#fff" stroke-width="1.6"><path d="M12 22s7-7 7-12a7 7 0 0 0-14 0c0 5 7 12 7 12z"/><circle cx="12" cy="10" r="2.5"/></svg><span>123 Your Adress Goes Here.<br>AU, 1234567</span></div>
  <div class="contact-row" style="margin-top:8px;font-size:17px"><svg width="17" height="17" viewBox="0 0 24 24" fill="none" stroke="#fff" stroke-width="1.6"><path d="M5 3h4l2 5-2.5 1.5a11 11 0 0 0 6 6L16 13l5 2v4a2 2 0 0 1-2 2A16 16 0 0 1 3 5a2 2 0 0 1 2-2z"/></svg><span>888 888 8888</span></div>
  <div class="contact-row" style="margin-top:13px"><svg width="17" height="17" viewBox="0 0 24 24" fill="none" stroke="#fff" stroke-width="1.6"><rect x="3" y="5" width="18" height="14"/><path d="M3 6l9 7 9-7"/></svg><span>info@dorianvellacourt.com</span></div>
</div>

<div class="abs rule"></div>
<div class="abs copy">Copyright © 2023 Dorian Vellacourt. All rights reserved.</div>

</body>
</html>
```